Inspirational Quotes Poster Set

Norbelle is a stylish coworking space, which has a design-oriented vintage look from the 60's with an industrial touch (www.norbelle-example.com) Norbelle Quote Poster Set of 16 posters. The poster should be typo oriented and rather simple. Reflecting a bit the clean billboard design from the sixties. Minimal / simple graphical elements

Target Market(s)

Startups and Entrepreneurs

Industry/Entity Type

Startup

Font styles to use
Sans Serif

Colors

Designer to choose colors to be used in the design.

Requirements
Must have
• Posters need to be on and very stylish

```html
<!DOCTYPE html>
<html lang="en">
<head>
<meta charset="utf-8">
<title>Norbelle Quote Poster Set – Keep Going</title>
<link href="https://fonts.googleapis.com/css2?family=Passion+One&family=Anton&family=Montserrat:wght@600&family=Lato:ital,wght@1,700&display=swap" rel="stylesheet">
<style>
  :root {
    --ink-slate: #252a33;
    --paper-white: #f7f8fa;
  }
  html, body {
    margin: 0;
    padding: 0;
    overflow: hidden;
    background: var(--ink-slate);
  }
  .poster {
    position: relative;
    width: 849px;
    height: 1200px;
    background: var(--ink-slate);
    color: var(--paper-white);
    overflow: hidden;
  }
  .quote {
    position: absolute;
    left: 192px;
    top: 0;
    margin: 0;
    font-weight: normal;
  }
  .quote span {
    position: absolute;
    left: 0;
    display: block;
    white-space: nowrap;
    line-height: 1;
  }
  .lead {
    font-family: "Passion One", "Arial Black", sans-serif;
    font-size: 74px;
    text-transform: uppercase;
    letter-spacing: 1px;
  }
  .lead--one   { top: 168px; }
  .lead--two   { top: 257px; }
  .lead--three { top: 343px; }
  .hell {
    top: 420px;
    font-family: "Anton", "Impact", sans-serif;
    font-size: 222px;
    letter-spacing: -2px;
    transform: scaleX(1.05);
    transform-origin: left top;
  }
  .keep, .going {
    font-family: "Montserrat", "Helvetica Neue", sans-serif;
    font-weight: 600;
    text-transform: uppercase;
  }
  .keep {
    top: 684px;
    font-size: 96px;
    letter-spacing: 0.3em;
  }
  .going {
    top: 800px;
    font-size: 81px;
    letter-spacing: 0.2em;
  }
  .attribution {
    position: absolute;
    left: 194px;
    top: 908px;
    margin: 0;
    font-family: "Lato", "Helvetica Neue", sans-serif;
    font-style: italic;
    font-weight: 700;
    font-size: 29px;
    line-height: 43px;
    letter-spacing: 0.5px;
  }
</style>
</head>
<body>
  <main class="poster">
    <h1 class="quote">
      <span class="lead lead--one">If you’re</span>
      <span class="lead lead--two">going</span>
      <span class="lead lead--three">through</span>
      <span class="hell">HELL,</span>
      <span class="keep">Keep</span>
      <span class="going">Going</span>
    </h1>
    <p class="attribution">Walter Ashcombe,<br>British Prime Minister</p>
  </main>
</body>
</html>
```